Trifold Brochure needed for Hearthline Counseling

Hi! We need to have a trifold brochure made.

We would like to see brochure designs that use our logo colors, which are khaki, chocolate brown, and gray.

The brochure should be a modern design and please use your creativity.

Brochure is a trifold brochure, size is 8.5 x 11 and full color.

The following attachment has the content to be used in the trifold brochure, as well as some possible pictures. I have also attached our logo.

We would like to use file #2 for sure (picture number 31759204) and add the quote from her...

"At first, I was reluctant about going to Hearthline. Once I got there, I was glad I went. I learned a lot and was treated like family the whole time." Marlene Oakes

Requirements
Must have
• Our logo
• Information should be listed exactly as the attached document
• You must stick with our logo colors

```html
<!DOCTYPE html>
<html lang="en">
<head>
<meta charset="utf-8">
<title>Hearthline Counseling – Trifold Brochure</title>
<link href="https://fonts.googleapis.com/css2?family=Raleway:wght@300;400;600;700&display=swap" rel="stylesheet">
<style>
  :root {
    --backdrop: #dfe2e2;
    --paper: #f7f6f3;
    --ink: #2e2e2c;
    --charcoal: #2b2b29;
    --slate: #6a6b69;
    --slate-light: #8b8c8a;
    --accent-red: #a3272d;
    --chocolate: #7b4a22;
    --khaki: #c9b68e;
    --white: #ffffff;
    --muted: #cfcfcc;
  }
  * { box-sizing: border-box; margin: 0; padding: 0; }
  html, body {
    width: 1200px; height: 891px; overflow: hidden;
    background: var(--backdrop);
    font-family: "Raleway", "Helvetica Neue", Arial, sans-serif;
  }
  .brochure {
    position: absolute; left: 94px; top: 50px;
    width: 1011px; height: 790px;
    display: flex;
    box-shadow: 0 12px 30px rgba(0,0,0,.18);
  }
  .panel { width: 337px; height: 100%; position: relative; overflow: hidden; }

  /* Panel 1 – introduction */
  .panel--intro { background: var(--paper); color: var(--ink); padding: 56px 32px 0 34px; }
  .intro-title { border-left: 4px solid var(--accent-red); padding-left: 14px; margin-bottom: 22px; }
  .intro-title h1 { font-weight: 300; font-size: 38px; line-height: 1; letter-spacing: .5px; }
  .intro-title span { display: block; font-size: 15px; letter-spacing: 2px; margin-top: 4px; }
  .intro-text { font-size: 12.5px; line-height: 1.45; font-weight: 300; margin-bottom: 20px; }
  .intro-text b { font-weight: 700; }
  .photo { display: block; }
  .photo--couple-park {
    width: 100%; height: 200px; margin-bottom: 36px;
    background: linear-gradient(135deg, #6fa24a 0%, #9cc46c 35%, #c5573f 62%, #3e6b2b 100%);
  }
  .points { list-style: none; }
  .point { display: flex; gap: 10px; margin-bottom: 38px; align-items: flex-start; }
  .point-num { font-size: 46px; font-weight: 300; line-height: .9; width: 28px; flex: none; }
  .point-text { font-size: 13px; font-weight: 300; line-height: 1.4; padding-top: 4px; }
  .point-text b { font-weight: 700; }

  /* Panel 2 – testimonial and education */
  .panel--education { background: var(--charcoal); color: var(--white); }
  .testimonial { padding: 30px 28px 22px; font-size: 12.5px; font-weight: 300; line-height: 1.5; font-style: normal; }
  .testimonial cite { display: block; margin-top: 8px; font-style: normal; font-weight: 600; text-align: right; }
  .photo--lake { width: 100%; height: 170px; background: linear-gradient(180deg, #dfe5e6 0%, #9fb0a9 40%, #55705f 60%, #b8c4c4 100%); }
  .edu-list { list-style: none; padding: 28px 28px 0 40px; }
  .edu-list li { font-size: 12.5px; line-height: 1.45; font-weight: 300; margin-bottom: 24px; }
  .edu-list li b { font-weight: 600; }

  /* Panel 3 – cover */
  .panel--cover {
    background: linear-gradient(180deg, #7a7b79 0%, #5f605e 100%);
    color: var(--white); text-align: center;
  }
  .cover-head { padding: 50px 26px 24px; }
  .brand { display: flex; align-items: center; justify-content: center; gap: 10px; }
  .brand-dot { width: 22px; height: 22px; border-radius: 50%; background: var(--khaki); }
  .brand-name { font-size: 30px; font-weight: 400; color: var(--white); }
  .brand-line { font-size: 10px; letter-spacing: 1.5px; margin-top: 8px; text-transform: lowercase; }
  .rule { border: 0; border-top: 1px solid var(--muted); width: 78%; margin: 14px auto; }
  .tagline { font-size: 19px; font-weight: 300; line-height: 1.3; }
  .photo--autumn { width: 100%; height: 190px; margin-top: 18px; background: linear-gradient(180deg, #c9b279 0%, #b3753a 55%, #8a3f19 100%); }
  .web { position: absolute; bottom: 44px; left: 0; right: 0; font-size: 11px; letter-spacing: .5px; color: var(--muted); }
</style>
</head>
<body>
<main class="brochure">

  <section class="panel panel--intro">
    <header class="intro-title">
      <h1>Hearthline</h1>
      <span>IS A...</span>
    </header>
    <p class="intro-text">Pro-active Opioid Education / not for addicts or problem patients. <b>Hearthline</b> only sees <b>Good Patients</b>, because problem patients and addicts <b>do not</b> want education they only want pills.</p>
    <div class="photo photo--couple-park" role="img" aria-label="Photo of a smiling couple embracing outdoors in a park"></div>
    <ol class="points">
      <li class="point"><span class="point-num">1</span><span class="point-text"><b>Good Patients</b> are Receptive to new information</span></li>
      <li class="point"><span class="point-num">2</span><span class="point-text">"Education" <b>Good Patients</b> need it the least! Therefore their minds are open and will soak it up the Most.</span></li>
      <li class="point"><span class="point-num">3</span><span class="point-text">Hearthline will <b>Teach You</b> and Hopefully <b>You</b> will <b>Teach someone else</b>. Better than that, maybe <b>Your</b> Education will <b>Save someone else</b></span></li>
    </ol>
  </section>

  <section class="panel panel--education">
    <blockquote class="testimonial">"At first, I was reluctant about going to Hearthline. Once I got there, I was glad I went. I learned a lot and was treated like family the whole time."
      <cite>Marlene Oakes</cite>
    </blockquote>
    <div class="photo photo--lake" role="img" aria-label="Photo of a calm lake with trees on the far shore"></div>
    <ul class="edu-list">
      <li><b>Education</b> on safe prescription use.</li>
      <li><b>Education</b> on dependence and risk.</li>
      <li><b>Education</b> is awareness and prevention.</li>
      <li><b>Educating</b> on the proper use of your medication and unneeded refills.</li>
      <li><b>Education</b> means safer homes.</li>
      <li>One Patient helps one Family, that Family helps a Neighborhood, which can affect One Community.</li>
    </ul>
  </section>

  <section class="panel panel--cover">
    <header class="cover-head">
      <div class="brand"><span class="brand-dot"></span><span class="brand-name">Hearthline</span></div>
      <p class="brand-line">a pro-active opioid education center</p>
      <hr class="rule">
      <p class="tagline">Making Solutions<br>"1" Patient at a Time here!</p>
      <hr class="rule">
    </header>
    <div class="photo photo--autumn" role="img" aria-label="Photo of an older couple lying together in autumn leaves"></div>
    <p class="web">www.hearthlinecounseling.org</p>
  </section>

</main>
</body>
</html>
```